Business Card for a Dental Office

The design should communicate integrity, quality and reliability. We also want the card look elegant, simple, but still stand out, different from the traditional-dental-office business card.

Business

```html
<!DOCTYPE html>
<html lang="en">
<head>
<meta charset="utf-8">
<title>Harbor Dental Studio – Business Card</title>
<link rel="stylesheet" href="https://fonts.googleapis.com/css2?family=Oswald:wght@500;600&family=Open+Sans:wght@400;600;700&display=swap">
<style>
  :root {
    --ink: #1d1d1b;
    --gold: #c9b02a;
    --gold-light: #e6d66a;
    --gold-dark: #a68d16;
    --text: #3a3a3a;
    --muted: #8a8a8a;
    --backdrop: #e8e5df;
  }
  * { margin: 0; padding: 0; box-sizing: border-box; }
  html, body { width: 1200px; height: 843px; overflow: hidden; }
  body {
    background: var(--backdrop);
    position: relative;
    font-family: "Open Sans", Arial, sans-serif;
    color: var(--text);
  }
  .card {
    position: absolute;
    width: 620px;
    height: 354px;
    background: linear-gradient(160deg, #ffffff 0%, #f6f6f6 100%);
    box-shadow: 0 10px 30px rgba(0,0,0,0.18);
  }
  .card--back { left: 60px; top: 50px; }
  .card--front { left: 520px; top: 440px; }

  .brand-name {
    font-family: "Oswald", "Arial Narrow", sans-serif;
    font-weight: 600;
    color: var(--ink);
    letter-spacing: 0.5px;
    line-height: 1;
    white-space: nowrap;
  }
  .tagline {
    font-family: "Open Sans", Arial, sans-serif;
    font-weight: 700;
    color: var(--gold);
    text-transform: uppercase;
    letter-spacing: 1px;
    line-height: 1;
    white-space: nowrap;
  }

  /* Back side */
  .back-brand {
    position: absolute;
    left: 0; right: 0; top: 128px;
    display: flex; align-items: center; justify-content: center; gap: 14px;
  }
  .brand-square {
    width: 44px; height: 44px;
    background: linear-gradient(135deg, var(--gold-light), var(--gold-dark));
  }
  .back-brand .brand-name { font-size: 30px; }
  .back-brand .tagline { font-size: 11px; margin-top: 4px; }
  .back-web {
    position: absolute;
    left: 0; right: 0; bottom: 58px;
    text-align: center;
    font-size: 13px;
    letter-spacing: 4px;
    color: var(--muted);
  }

  /* Front side */
  .front-square {
    position: absolute;
    left: 44px; top: 40px;
    width: 200px; height: 200px;
    background: linear-gradient(135deg, var(--gold-light) 0%, var(--gold) 55%, var(--gold-dark) 100%);
  }
  .contact {
    position: absolute;
    right: 30px; top: 30px;
    text-align: right;
    font-size: 14px;
    line-height: 1.3;
  }
  .contact__name { font-weight: 700; font-size: 19px; color: var(--ink); }
  .contact__title { font-size: 14px; color: var(--gold); margin-bottom: 6px; }
  .contact__address { margin-bottom: 2px; }
  .contact__line {
    display: flex; justify-content: flex-end; align-items: center; gap: 10px;
    height: 20px;
  }
  .contact__line svg { width: 13px; height: 13px; fill: var(--ink); flex: none; }
  .front-brand {
    position: absolute;
    right: 30px; bottom: 30px;
  }
  .front-brand .brand-name { font-size: 34px; }
  .front-brand .tagline { font-size: 12px; margin-top: 6px; }
</style>
</head>
<body>

<section class="card card--back" aria-label="Business card, back side">
  <div class="back-brand">
    <div class="brand-square" aria-hidden="true"></div>
    <div>
      <div class="brand-name">HARBOR DENTAL STUDIO</div>
      <div class="tagline">Gentle care for every bright smile</div>
    </div>
  </div>
  <div class="back-web">www.harbordental.com</div>
</section>

<section class="card card--front" aria-label="Business card, front side">
  <div class="front-square" aria-hidden="true"></div>

  <div class="contact">
    <div class="contact__name">Daniel Reyes</div>
    <div class="contact__title">CEO/Founder</div>
    <div class="contact__address">214 Birchwood Avenue<br>Juneau, Alaska 99801</div>
    <div class="contact__line">555 204 1187
      <svg viewBox="0 0 24 24" aria-label="phone"><path d="M6.6 10.8a15.1 15.1 0 0 0 6.6 6.6l2.2-2.2c.3-.3.7-.4 1-.2 1.1.4 2.3.6 3.6.6.6 0 1 .4 1 1V20c0 .6-.4 1-1 1A17 17 0 0 1 3 4c0-.6.4-1 1-1h3.5c.6 0 1 .4 1 1 0 1.3.2 2.5.6 3.6.1.3 0 .7-.2 1z"/></svg>
    </div>
    <div class="contact__line">555 382 6049
      <svg viewBox="0 0 24 24" aria-label="mobile"><path d="M7 1h10a2 2 0 0 1 2 2v18a2 2 0 0 1-2 2H7a2 2 0 0 1-2-2V3a2 2 0 0 1 2-2zm0 3v14h10V4zm5 15.5a1.2 1.2 0 1 0 0 2.4 1.2 1.2 0 0 0 0-2.4z"/></svg>
    </div>
    <div class="contact__line">555 917 3325
      <svg viewBox="0 0 24 24" aria-label="fax"><path d="M6 2h12v6H6zM4 9h16a2 2 0 0 1 2 2v7h-4v4H6v-4H2v-7a2 2 0 0 1 2-2zm4 7v4h8v-4z"/></svg>
    </div>
    <div class="contact__line">hello@harbordental.com
      <svg viewBox="0 0 24 24" aria-label="email"><path d="M2 5h20v14H2zm2 2v.5l8 5 8-5V7l-8 5z"/></svg>
    </div>
    <div class="contact__line">www.harbordental.com
      <svg viewBox="0 0 24 24" aria-label="website"><path d="M12 2a10 10 0 1 0 0 20 10 10 0 0 0 0-20zm0 2c.8 1.1 1.5 2.5 1.9 4h-3.8c.4-1.5 1.1-2.9 1.9-4zM4.3 14a8 8 0 0 1 0-4h3.4a16 16 0 0 0 0 4zm15.4 0h-3.4a16 16 0 0 0 0-4h3.4a8 8 0 0 1 0 4zM12 20c-.8-1.1-1.5-2.5-1.9-4h3.8c-.4 1.5-1.1 2.9-1.9 4zm2.3-6H9.7a14 14 0 0 1 0-4h4.6a14 14 0 0 1 0 4z"/></svg>
    </div>
  </div>

  <div class="front-brand">
    <div class="brand-name">HARBOR DENTAL STUDIO</div>
    <div class="tagline">Gentle care for every bright smile</div>
  </div>
</section>

</body>
</html>
```